Bright Harbor Painting and Remodeling needs a business card

Business card should have company logo. I will upload two different logos and let me see which one is a better design for the business card.

Name of company: Bright Harbor Painting and Remodeling
Address: 4826 NW 61st st Suite 214
Miami, FL 33172

local phone: (305) 555-0143
toll free (855) 555-0176
fax (866) 555-0128

email: darla@brightharborcoats.example

not sure if i should include social media links or names on the business card.

company does interior and exterior painting, pressure washing, wall paper removal, drywall and stucco repair, staining,

We give free estimates.

I want a two sided business card.

Not sure if all this information is necessary for the business card. Designer can pick out whatever information they deem is important for a consumer to see on the business card.

Anticipating on the business card to be printed on nice quality.

I will upload an image of one of the logos on a type of business card surface. That idea can be used as well. Be creative. Business card should be professional but very nice and eye catching.

remove drywall and stucco repair and replace with tile installation

Industry/Entity Type

Business

Contact Information for Business Card

Miami, FL 33172

toll free (855) 555-0176
fax (866) 555-0128

company does interior and exterior painting, pressure washing, wall paper removal, drywall and stucco repair, staining, tile removal, *specializing in vinyl floor removal

free estimates.

Requirements
Must have
• Profesional font

```html
<!DOCTYPE html>
<html lang="en">
<head>
<meta charset="utf-8">
<title>Bright Harbor Painting and Remodeling – Business Card</title>
<link href="https://fonts.googleapis.com/css2?family=Open+Sans:wght@400;600;700&display=swap" rel="stylesheet">
<style>
  :root {
    --stage: #e9e9ec;
    --card: #ffffff;
    --violet: #8e7dd3;
    --lime: #8ede5c;
    --ink: #1f1f24;
    --white: #ffffff;
    --shadow: rgba(20, 20, 30, 0.18);
  }
  * { margin: 0; padding: 0; box-sizing: border-box; }
  html, body {
    width: 1200px;
    height: 977px;
    overflow: hidden;
    background: var(--stage);
    font-family: "Open Sans", Arial, sans-serif;
  }
  .sheet {
    width: 1200px;
    height: 977px;
    display: flex;
    flex-direction: column;
    align-items: center;
    justify-content: center;
    gap: 48px;
  }
  .card {
    position: relative;
    width: 620px;
    height: 354px;
    background: var(--card);
    box-shadow: 0 10px 28px var(--shadow);
    overflow: hidden;
  }

  /* Front side */
  .card--front {
    display: flex;
    align-items: center;
    justify-content: center;
  }
  .brand {
    display: flex;
    align-items: center;
    gap: 12px;
    color: var(--ink);
    font-weight: 600;
  }
  .brand__dot {
    width: 18px;
    height: 18px;
    border-radius: 50%;
    background: var(--violet);
    flex: none;
  }
  .brand__name { line-height: 1.25; }
  .card--front .brand__name { font-size: 26px; text-align: center; }
  .brand__line { display: block; }

  /* Back side */
  .card__arc {
    position: absolute;
    inset: 0;
    width: 620px;
    height: 354px;
  }
  .contact {
    position: absolute;
    left: 52px;
    top: 58px;
    color: var(--white);
  }
  .contact__name {
    font-size: 21px;
    font-weight: 700;
    letter-spacing: 0.2px;
  }
  .contact__role {
    font-size: 13px;
    font-weight: 600;
    margin: 2px 0 0 8px;
  }
  .contact__address {
    font-size: 13px;
    line-height: 1.45;
    margin: 16px 0 14px 18px;
  }
  .contact__list { list-style: none; }
  .contact__item {
    display: flex;
    align-items: center;
    gap: 14px;
    font-size: 13.5px;
    line-height: 25px;
  }
  .contact__icon {
    width: 15px;
    height: 15px;
    flex: none;
    fill: var(--white);
  }
  .card--back .brand {
    position: absolute;
    left: 424px;
    right: 18px;
    top: 0;
    bottom: 40px;
    justify-content: center;
    gap: 9px;
  }
  .card--back .brand__dot { width: 14px; height: 14px; }
  .card--back .brand__name { font-size: 16px; text-align: left; }
</style>
</head>
<body>
<main class="sheet">

  <section class="card card--front" aria-label="Card front">
    <div class="brand">
      <span class="brand__dot"></span>
      <p class="brand__name">
        <span class="brand__line">Bright Harbor</span>
        <span class="brand__line">Painting and Remodeling</span>
      </p>
    </div>
  </section>

  <section class="card card--back" aria-label="Card back">
    <svg class="card__arc" viewBox="0 0 620 354" aria-hidden="true">
      <circle cx="-20" cy="185" r="420" fill="none" stroke="var(--lime)" stroke-width="9"/>
      <circle cx="-20" cy="185" r="412" fill="var(--white)"/>
      <circle cx="-20" cy="185" r="406" fill="var(--violet)"/>
    </svg>

    <div class="contact">
      <h1 class="contact__name">Darla Reyes</h1>
      <p class="contact__role">Manager</p>
      <p class="contact__address">4826 NW 61st st Suite 214<br>Miami, FL 33172</p>
      <ul class="contact__list">
        <li class="contact__item">
          <svg class="contact__icon" viewBox="0 0 16 16" aria-hidden="true"><path d="M3.5 1l2.6 2.7-1.4 2c.9 1.9 2.4 3.4 4.3 4.3l2-1.4L13.7 11.2l-1.6 2.6C7 13.6 2.4 9 2.2 3.9z"/></svg>
          <span>(305) 555-0143</span>
        </li>
        <li class="contact__item">
          <svg class="contact__icon" viewBox="0 0 16 16" aria-hidden="true"><path d="M4.5 1h7a1 1 0 0 1 1 1v12a1 1 0 0 1-1 1h-7a1 1 0 0 1-1-1V2a1 1 0 0 1 1-1zm.5 2v9h6V3zm3 10a.8.8 0 1 0 0 .01z"/></svg>
          <span>(855) 555-0176</span>
        </li>
        <li class="contact__item">
          <svg class="contact__icon" viewBox="0 0 16 16" aria-hidden="true"><path d="M4 1h6l2 2v3H4zM2 7h12a1 1 0 0 1 1 1v5H1V8a1 1 0 0 1 1-1zm2 3v3h8v-3z"/></svg>
          <span>(866) 555-0128</span>
        </li>
        <li class="contact__item">
          <svg class="contact__icon" viewBox="0 0 16 16" aria-hidden="true"><path d="M1 3h14v1.2L8 9 1 4.2zm0 2.6l7 4.8 7-4.8V13H1z"/></svg>
          <span>darla@brightharborcoats.example</span>
        </li>
        <li class="contact__item">
          <svg class="contact__icon" viewBox="0 0 16 16" aria-hidden="true"><path d="M8 1a7 7 0 1 1 0 14A7 7 0 0 1 8 1zm-2.5 4a1 1 0 1 0 0 .01zm5 0a1 1 0 1 0 0 .01zM5.5 9a1 1 0 1 0 0 .01zm5 0a1 1 0 1 0 0 .01zM8 7a1 1 0 1 0 0 .01zm0 4a1 1 0 1 0 0 .01z"/></svg>
          <span>www.brightharborcoats.example</span>
        </li>
      </ul>
    </div>

    <div class="brand">
      <span class="brand__dot"></span>
      <p class="brand__name">
        <span class="brand__line">Bright Harbor</span>
        <span class="brand__line">Painting and</span>
        <span class="brand__line">Remodeling</span>
      </p>
    </div>
  </section>

</main>
</body>
</html>
```